Clearbrook Turf Systems LLC Business Card

Ok, first off let me thank you for taking the time to participate in this project !! I have my business logo that I want incorporated into business card design . My irrigation business is located in a very upscale part of town and we do high end homes . So with that said I'm planning on these cards being plastic credit card type cards. I would like them to be two sided . I'm thinking something bold , yet classy and clean . Not too busy . We do different types of work . 80% irrigation service and installation . 15% landscape lighting and the other 5% drainage and hardscapes ! I have a website that I want listed on it as well as our address , phone number and of course my name and title .
Updates

Target Market(s)

Upscale homeowners and architects

Industry/Entity Type

Landscape

Requirements
Must have
• Company logo, website, address , phone number , name , title , services offered

Www.ClearbrookTurfSystems.example
Marcus Elwood owner
205-481-5926
Clearbrook Turf Systems LLC
P.O. Box 947152
Larkspur Glen, Vermont 05901

```html
<!DOCTYPE html>
<html lang="en">
<head>
<meta charset="utf-8">
<title>Clearbrook Turf Systems LLC – Business Card</title>
<link href="https://fonts.googleapis.com/css2?family=PT+Sans:ital,wght@0,400;0,700;1,400;1,700&display=swap" rel="stylesheet">
<style>
  :root {
    --page: #eeeeec;
    --card: #ffffff;
    --brand-green: #62a93a;
    --brand-blue: #1e9bd7;
    --ink: #111111;
    --soft-ink: #222222;
    --on-blue: #ffffff;
  }
  * { margin: 0; padding: 0; box-sizing: border-box; }
  html, body { width: 1200px; height: 999px; overflow: hidden; }
  body {
    background: var(--page);
    font-family: "PT Sans", sans-serif;
    position: relative;
  }
  .card {
    position: absolute;
    width: 510px;
    height: 290px;
    background: var(--card);
    box-shadow: 0 4px 14px rgba(0,0,0,.18);
    overflow: hidden;
  }
  .card--front { left: 75px; top: 355px; }
  .card--back  { left: 615px; top: 355px; }

  .brand {
    display: flex; align-items: center; gap: 10px;
    position: absolute;
  }
  .brand__dot {
    border-radius: 50%;
    background: var(--brand-blue);
    flex: none;
  }
  .brand__name {
    font-weight: 700;
    color: var(--brand-green);
    white-space: nowrap;
  }

  .card--front .brand { left: 0; right: 0; top: 98px; justify-content: center; }
  .card--front .brand__dot { width: 46px; height: 46px; }
  .card--front .brand__name { font-size: 30px; }
  .front__web {
    position: absolute; left: 0; right: 0; top: 168px;
    text-align: center;
    color: var(--brand-blue);
    font-size: 20px;
  }

  .back__panel { position: absolute; inset: 0; }
  .card--back .brand {
    left: 20px; top: 36px; width: 280px;
    flex-direction: column; gap: 8px;
  }
  .card--back .brand__dot { width: 68px; height: 68px; }
  .card--back .brand__name { font-size: 22px; line-height: 26px; }

  .services {
    position: absolute; left: 30px; top: 182px;
    font-style: italic; font-weight: 700;
    font-size: 15px; line-height: 20px;
    color: var(--ink);
    list-style: none;
  }
  .services__title { color: var(--brand-blue); }
  .services__item::before { content: "• "; color: var(--brand-blue); }

  .contact {
    position: absolute; right: 30px; text-align: right;
    font-style: italic;
  }
  .contact__name { top: 32px; font-weight: 700; font-size: 19px; line-height: 22px; color: var(--ink); }
  .contact__title { top: 54px; font-size: 14px; line-height: 18px; color: var(--soft-ink); }
  .contact__address { top: 154px; font-weight: 700; font-size: 13px; line-height: 17px; color: var(--on-blue); }
  .contact__line {
    right: 12px;
    display: flex; align-items: center; justify-content: flex-end; gap: 5px;
    color: var(--on-blue); font-weight: 700;
  }
  .contact__phone { top: 220px; font-size: 17px; line-height: 22px; }
  .contact__web { top: 243px; font-size: 13px; line-height: 17px; }
</style>
</head>
<body>

<section class="card card--front" aria-label="Card front">
  <div class="brand">
    <span class="brand__dot"></span>
    <span class="brand__name">Clearbrook Turf Systems</span>
  </div>
  <p class="front__web">www.clearbrookturfsystems.example</p>
</section>

<section class="card card--back" aria-label="Card back">
  <svg class="back__panel" width="510" height="290" viewBox="0 0 510 290" aria-hidden="true">
    <defs>
      <linearGradient id="panelFill" x1="0" y1="0" x2="0" y2="1">
        <stop offset="0" stop-color="#dff0fb"/>
        <stop offset="0.25" stop-color="#a9dbf5"/>
        <stop offset="0.42" stop-color="#10a2e0"/>
        <stop offset="0.74" stop-color="#1e6fb8"/>
        <stop offset="0.75" stop-color="#1f5aa6"/>
        <stop offset="1" stop-color="#1f5aa6"/>
      </linearGradient>
      <linearGradient id="arcFill" x1="0" y1="0" x2="0" y2="1">
        <stop offset="0" stop-color="#6fae35"/>
        <stop offset="1" stop-color="#d9ebb8"/>
      </linearGradient>
    </defs>
    <path d="M306 0 C 342 80 338 195 190 290 L510 290 L510 0 Z" fill="url(#arcFill)"/>
    <path d="M316 0 C 352 82 348 198 205 290 L510 290 L510 0 Z" fill="url(#panelFill)"/>
  </svg>

  <div class="brand">
    <span class="brand__dot"></span>
    <span class="brand__name">Clearbrook Turf Systems</span>
  </div>

  <ul class="services">
    <li class="services__title">Services Offered:</li>
    <li class="services__item">Irrigation Service &amp; Installation</li>
    <li class="services__item">Landscape Lighting</li>
    <li class="services__item">Drainage &amp; Hardscapes</li>
  </ul>

  <p class="contact contact__name">Marcus Elwood</p>
  <p class="contact contact__title">Owner</p>
  <p class="contact contact__address">P.O. Box 947152<br>Larkspur Glen<br>Vermont 05901</p>

  <p class="contact contact__line contact__phone">205-481-5926
    <svg width="16" height="12" viewBox="0 0 16 12" aria-hidden="true"><path d="M1 4 Q8 -1 15 4 L13 6 L11 4.5 L11 3 Q8 2 5 3 L5 4.5 L3 6 Z" fill="#fff"/><rect x="4" y="7" width="8" height="4" rx="1" fill="#fff"/></svg>
  </p>
  <p class="contact contact__line contact__web">www.clearbrookturfsystems.example
    <svg width="15" height="15" viewBox="0 0 16 16" aria-hidden="true"><g fill="none" stroke="#fff" stroke-width="1.3"><circle cx="8" cy="8" r="6.5"/><ellipse cx="8" cy="8" rx="3" ry="6.5"/><path d="M1.5 8h13M2.5 5h11M2.5 11h11"/></g></svg>
  </p>
</section>

</body>
</html>
```